Business Cards and Stationery for Borvexa engineering company.
Borvexa
Business Cards and Stationery for Borvexa engineering company. - Engineering
Creative Brief
Simple
Delgado Tarvin
Velmora Region, Kestrovsk-on-Lune, st. Korvell, 283/7 office 42
tarvindelgado@mailbrook.example
logo on different backgrounds

```html
<!DOCTYPE html>
<html lang="en">
<head>
<meta charset="utf-8">
<title>Borvexa — Business Cards</title>
<link href="https://fonts.googleapis.com/css2?family=Exo+2:ital,wght@0,700;1,400&family=Roboto:wght@400;500&display=swap" rel="stylesheet">
<style>
  :root {
    --bg-top: #f1f2f4;
    --bg-bottom: #d9dbdf;
    --card-white: #ffffff;
    --brand-blue: #2a86c8;
    --brand-blue-deep: #1a6fb0;
    --brand-blue-light: #4aa6e0;
    --swoosh-grey: #9aa0a8;
    --ink-grey: #6b7077;
    --ink-white: #ffffff;
  }
  * { box-sizing: border-box; margin: 0; padding: 0; }
  html, body { width: 1200px; height: 984px; overflow: hidden; }
  body {
    background: linear-gradient(180deg, var(--bg-top), var(--bg-bottom));
    font-family: "Roboto", Arial, sans-serif;
    position: relative;
  }
  .card {
    position: absolute;
    left: 250px;
    width: 700px;
    height: 400px;
    border-radius: 22px;
    background: var(--card-white);
    overflow: hidden;
    box-shadow: 0 10px 30px rgba(0,0,0,0.18);
  }
  .card-front { top: 70px; }
  .card-back { top: 514px; }

  /* Front */
  .front-mark {
    position: absolute;
    left: 0; right: 0; top: 90px;
    display: flex; flex-direction: column; align-items: center;
  }
  .mark-circle {
    width: 120px; height: 120px; border-radius: 50%;
    background: var(--brand-blue);
  }
  .front-name {
    margin-top: 16px;
    font-family: "Exo 2", Arial, sans-serif;
    font-weight: 700;
    font-size: 34px;
    color: var(--brand-blue);
  }
  .front-web {
    margin-top: 22px;
    font-size: 17px;
    letter-spacing: 6px;
    color: var(--ink-grey);
  }

  /* Back */
  .back-band { position: absolute; inset: 0; }
  .back-brand {
    position: absolute; left: 40px; top: 36px;
    display: flex; align-items: center; gap: 14px;
  }
  .brand-circle {
    width: 64px; height: 64px; border-radius: 50%;
    background: var(--brand-blue);
  }
  .brand-name {
    font-family: "Exo 2", Arial, sans-serif;
    font-weight: 700;
    font-size: 56px;
    color: var(--brand-blue);
    line-height: 1;
  }
  .holder-name {
    position: absolute; left: 118px; top: 104px;
    font-family: "Exo 2", Arial, sans-serif;
    font-style: italic;
    font-size: 17px;
    color: var(--ink-grey);
  }
  .address {
    position: absolute; left: 40px; top: 268px;
    font-style: normal;
    font-size: 14px;
    line-height: 1.5;
    color: var(--ink-white);
  }
  .contacts {
    position: absolute; right: 40px; bottom: 28px;
    list-style: none;
    font-size: 14px;
    color: var(--ink-white);
  }
  .contacts li { display: flex; align-items: center; gap: 8px; line-height: 1.6; }
  .contacts svg { width: 14px; height: 14px; flex: none; }
</style>
</head>
<body>

<section class="card card-front" aria-label="Business card front">
  <div class="front-mark">
    <div class="mark-circle"></div>
    <div class="front-name">Borvexa</div>
    <div class="front-web">www.borvexadomain.example</div>
  </div>
</section>

<section class="card card-back" aria-label="Business card back">
  <svg class="back-band" viewBox="0 0 700 400" preserveAspectRatio="none" aria-hidden="true">
    <defs>
      <linearGradient id="bandBlue" x1="0" y1="0" x2="0" y2="1">
        <stop offset="0" stop-color="var(--brand-blue-light)"/>
        <stop offset="1" stop-color="var(--brand-blue-deep)"/>
      </linearGradient>
      <linearGradient id="swooshGrey" x1="0" y1="0" x2="1" y2="0">
        <stop offset="0" stop-color="#e4e6e9"/>
        <stop offset="0.5" stop-color="var(--swoosh-grey)"/>
        <stop offset="1" stop-color="#d0d3d7"/>
      </linearGradient>
    </defs>
    <path d="M0,150 C180,150 420,112 700,82 L700,104 C430,132 200,168 0,172 Z" fill="url(#swooshGrey)"/>
    <path d="M0,205 C220,185 440,150 700,118 L700,400 L0,400 Z" fill="url(#bandBlue)"/>
  </svg>

  <div class="back-brand">
    <div class="brand-circle"></div>
    <div class="brand-name">Borvexa</div>
  </div>
  <div class="holder-name">Delgado Tarvin</div>

  <address class="address">
    Velmora Region, Kestrovsk-on-Lune,<br>
    st. Korvell, 283/7 office 42
  </address>

  <ul class="contacts">
    <li>
      <svg viewBox="0 0 16 16"><circle cx="8" cy="8" r="8" fill="#fff"/><path d="M5 4.5l1.6-.5 1 2-1 .8a5 5 0 0 0 2.6 2.6l.8-1 2 1-.5 1.6C8 11.5 4.5 8 5 4.5z" fill="var(--brand-blue)"/></svg>
      89170046213
    </li>
    <li>
      <svg viewBox="0 0 16 16"><circle cx="8" cy="8" r="8" fill="#fff"/><rect x="4" y="5" width="8" height="6" rx="1" fill="var(--brand-blue)"/><path d="M4.3 5.4L8 8.4l3.7-3" stroke="#fff" stroke-width="0.9" fill="none"/></svg>
      tarvindelgado@mailbrook.example
    </li>
    <li>
      <svg viewBox="0 0 16 16"><circle cx="8" cy="8" r="8" fill="#fff"/><circle cx="8" cy="8" r="4.5" stroke="var(--brand-blue)" stroke-width="1" fill="none"/><path d="M3.5 8h9M8 3.5c-2 2.5-2 6.5 0 9M8 3.5c2 2.5 2 6.5 0 9" stroke="var(--brand-blue)" stroke-width="0.9" fill="none"/></svg>
      www.borvexa.example
    </li>
  </ul>
</section>

</body>
</html>
```